The Brightwater Hour with Dale Morrow

Create Podcast Art for Podvale. My podcast is about overcoming adversities.

Everyone's adversity is different and there's no one-size-fits-all solution, but when you hear someone's else's story of resilience and add a little salt to it, you can find the inspiration you need to write a new ending to your struggle.

Maybe you're going through something right now and you're afraid:

● You won't be successful
● People are talking behind your back
● You'll never get the help you need
● You're not a good husband or wife
● Your child is out of control and you'll never get through to him or her
● There isn't a light at the end of your tunnel
● You'll never get your finances out of the red
● Your spouse won't ever see things your way
● The world is never gonna change

Every story we tell on The Brightwater Hour podcast challenges those thoughts, because everyday people going through everyday stuff just like you show us otherwise.

This podcast is for you. And, it's different.

Most interviews I do, I try to go on location and interview in person.

You might not see us together on the screen,
but you'll sense the raw sincerity and closeness of a side-by-side interview through your speakers.

The colors I have chosen below are close to the website colors. If you need a better view of that go here http://www.dalemorrowvoice.com

I've attached two pictures for the podcast. I'm not sure which one to use just yet so I put them both here to see what i created by your great people!

Target Market(s)

People who are currently going through an Advesirty or have been through one. 28 - 40 age group.

Colors
ec1f27
ffffff
000000
fbee3e

Requirements
Must have
• Eye appeal and The title "The Brightwater Hour" with Dale Morrow
• HAS to be stand-out, and it HAS to give a great first impression.
Nice to have
• The colors I have chosen are close to the website colors.

```html
<!DOCTYPE html>
<html lang="en">
<head>
<meta charset="utf-8">
<title>The Brightwater Hour — Podcast Art</title>
<link rel="stylesheet" href="https://fonts.googleapis.com/css2?family=Teko:wght@500&family=Archivo+Black&display=swap">
<style>
  :root {
    --black: #000000;
    --ink: #07080b;
    --red: #ec1f27;
    --white: #ffffff;
    --yellow: #fbee3e;
    --haze-top: #55514f;
    --wall: #cbb3a6;
    --wall-light: #e7d7cc;
    --sepia-mid: #c98a62;
    --sepia-deep: #a8562a;
  }
  * { margin: 0; padding: 0; box-sizing: border-box; }
  html, body { width: 1200px; height: 1200px; overflow: hidden; background: var(--black); }

  .cover {
    position: relative;
    width: 1200px;
    height: 1200px;
    overflow: hidden;
    background: var(--ink);
  }

  .host-photo {
    position: absolute;
    inset: 0;
    background:
      radial-gradient(ellipse 360px 260px at 790px 270px, rgba(231,215,204,0.9) 0%, rgba(231,215,204,0) 100%),
      radial-gradient(ellipse 420px 560px at 880px 860px, var(--sepia-deep) 0%, rgba(168,86,42,0.75) 50%, rgba(168,86,42,0) 90%),
      linear-gradient(180deg, var(--haze-top) 0%, var(--wall) 30%, var(--wall-light) 45%, var(--sepia-mid) 72%, var(--sepia-deep) 100%);
  }

  .left-shade {
    position: absolute;
    inset: 0;
    background:
      linear-gradient(90deg, var(--ink) 0%, var(--ink) 12%, rgba(7,8,11,0.9) 22%, rgba(7,8,11,0.5) 36%, rgba(7,8,11,0) 50%),
      linear-gradient(180deg, rgba(7,8,11,0.75) 0%, rgba(7,8,11,0.2) 25%, rgba(7,8,11,0) 40%);
  }

  .stripe { position: absolute; top: 0; height: 1200px; }
  .stripe--red {
    left: 100px; width: 14px;
    background: linear-gradient(180deg, var(--red) 0%, rgba(236,31,39,0.25) 30%, rgba(236,31,39,0.1) 55%, var(--red) 85%, var(--red) 100%);
  }
  .stripe--white {
    left: 132px; width: 14px;
    background: linear-gradient(180deg, var(--white) 0%, rgba(255,255,255,0.3) 30%, rgba(255,255,255,0.12) 55%, var(--white) 85%, var(--white) 100%);
  }
  .stripe--yellow {
    left: 154px; width: 11px;
    background: linear-gradient(180deg, var(--yellow) 0%, rgba(251,238,62,0.3) 30%, rgba(251,238,62,0.12) 55%, var(--yellow) 85%, var(--yellow) 100%);
  }

  .artwork { position: absolute; inset: 0; width: 1200px; height: 1200px; }

  .title-line {
    font-family: "Teko", "Arial Narrow", sans-serif;
    font-weight: 500;
    font-size: 178px;
    text-transform: uppercase;
  }
  .title-line--shadow { fill: var(--red); opacity: 0.8; }
  .title-line--face {
    fill: var(--black);
    stroke: var(--white);
    stroke-width: 4px;
    paint-order: stroke;
  }

  .host-name {
    font-family: "Archivo Black", "Arial Black", sans-serif;
    font-size: 44px;
    fill: var(--yellow);
    stroke: var(--black);
    stroke-width: 3px;
    paint-order: stroke;
  }
</style>
</head>
<body>
  <main class="cover">
    <div class="host-photo" role="img" aria-label="Sepia-toned portrait of the host seated on brick steps in front of a brick wall, wearing a sweater over a checked collared shirt, hands clasped"></div>
    <div class="left-shade"></div>

    <div class="stripe stripe--red"></div>
    <div class="stripe stripe--white"></div>
    <div class="stripe stripe--yellow"></div>

    <svg class="artwork" viewBox="0 0 1200 1200" role="group" aria-label="The Brightwater Hour with Dale Morrow">
      <defs>
        <radialGradient id="flare-glow">
          <stop offset="0" stop-color="#ffffff" stop-opacity="1"/>
          <stop offset="0.25" stop-color="#ffe08a" stop-opacity="0.9"/>
          <stop offset="1" stop-color="#f5a623" stop-opacity="0"/>
        </radialGradient>
        <linearGradient id="flare-ray-h" x1="0" x2="1">
          <stop offset="0" stop-color="#ffd36b" stop-opacity="0"/>
          <stop offset="0.5" stop-color="#fff6d0" stop-opacity="1"/>
          <stop offset="1" stop-color="#ffd36b" stop-opacity="0"/>
        </linearGradient>
      </defs>

      <g class="show-title">
        <text class="title-line title-line--shadow" x="70" y="516" textLength="196" lengthAdjust="spacingAndGlyphs">The</text>
        <text class="title-line title-line--shadow" x="74" y="668" textLength="470" lengthAdjust="spacingAndGlyphs">Brightwater</text>
        <text class="title-line title-line--shadow" x="74" y="812" textLength="240" lengthAdjust="spacingAndGlyphs">Hour</text>

        <text class="title-line title-line--face" x="62" y="512" textLength="196" lengthAdjust="spacingAndGlyphs">The</text>
        <text class="title-line title-line--face" x="66" y="664" textLength="470" lengthAdjust="spacingAndGlyphs">Brightwater</text>
        <text class="title-line title-line--face" x="66" y="808" textLength="240" lengthAdjust="spacingAndGlyphs">Hour</text>
      </g>

      <g class="lens-flare" transform="translate(256 676)">
        <circle r="42" fill="url(#flare-glow)"/>
        <rect x="-90" y="-1.5" width="180" height="3" fill="url(#flare-ray-h)"/>
        <rect x="-90" y="-1.5" width="180" height="3" fill="url(#flare-ray-h)" transform="rotate(90)"/>
        <rect x="-130" y="-1" width="260" height="2" fill="url(#flare-ray-h)" transform="rotate(-40)"/>
        <rect x="-70" y="-1" width="140" height="2" fill="url(#flare-ray-h)" transform="rotate(35)"/>
        <circle r="5" fill="#ffffff"/>
      </g>

      <text class="host-name" x="64" y="870" textLength="348" lengthAdjust="spacingAndGlyphs">Dale Morrow</text>
    </svg>
  </main>
</body>
</html>
```